Web Design for an Online Dating Web Site

We need an uncoded web design for a new online dating web site called zMatchy.net. Simplicity and boldness are the key factors in the successful design.
Please look at the requirements document attached for details.
Updates
Dear all,
Please AVOID USING A PICTURE OF A HAPPY COUPLE ON THE HOME PAGE of the site. We highly want to move away from this space as it makes our web site just like another dating web site.
We like something simple with web 2.0 look and feel. The examples in the Requirements Document are exactly the design we are after.
Regards
Tarn
Industry/Entity Type
Dating
Look and feel
Each slider illustrates characteristics of the customer's brand and the style your logo design should communicate.

```html
<!DOCTYPE html>
<html lang="en">
<head>
<meta charset="utf-8">
<title>zMatchy.net</title>
<link href="https://fonts.googleapis.com/css2?family=Rokkitt:wght@400;500;700&display=swap" rel="stylesheet">
<style>
:root{
  --cream:#f8eed8;
  --paper:#f8f5ee;
  --lime:#c8dc70;
  --green:#6cb32c;
  --green-dark:#4f8c12;
  --cyan:#2fc0e8;
  --cyan-dark:#1796c0;
  --pink:#e8198b;
  --grey:#808080;
  --grey-dark:#5f5f5f;
  --text:#555;
  --box:#f7f3e4;
  --box-line:#d8e4a0;
}
*{box-sizing:border-box;margin:0;padding:0}
html,body{width:900px;height:1200px;overflow:hidden}
body{position:relative;background:var(--paper);font-family:Arial,Helvetica,sans-serif;color:var(--text)}
.slab{font-family:"Rokkitt",Georgia,serif}
.abs{position:absolute}

.header{left:0;top:0;width:900px;height:138px;background:var(--cream);border-top:6px dotted #999}
.brand{left:88px;top:42px;font-family:"Rokkitt",Georgia,serif;font-size:52px;font-weight:700;color:var(--pink);letter-spacing:-1px}
.brand-sub{left:190px;top:92px;font-size:10px;color:#777}
.nav a{position:absolute;top:66px;font-family:"Rokkitt",Georgia,serif;font-size:20px;color:var(--green);text-decoration:none}
.btn{position:absolute;display:flex;align-items:center;justify-content:center;color:#fff;font-family:"Rokkitt",Georgia,serif;border-radius:14px;box-shadow:0 2px 3px rgba(0,0,0,.25)}
.btn-green{background:linear-gradient(#8cc63a,var(--green-dark))}
.btn-cyan{background:linear-gradient(#5fd6f4,var(--cyan-dark))}
.btn-pink{background:linear-gradient(#ff4fb0,var(--pink))}

.hero{left:0;top:138px;width:900px;height:250px;background:var(--paper)}
.hero-frame{left:95px;top:165px;width:358px;height:198px;background:#fff;border-radius:14px;box-shadow:0 1px 4px rgba(0,0,0,.15);padding:8px}
.hero-photo{width:100%;height:100%;border-radius:8px;background:radial-gradient(circle at 75% 25%,#fff6d8,#f2c98a 40%,#c9a27c 75%,#8a9ba0)}
.hero-title{left:468px;top:168px;font-size:29px;color:var(--cyan)}
.hero-sub{left:469px;top:206px;font-size:11.5px;color:var(--cyan)}
.hero-copy{left:469px;top:240px;width:327px;font-family:"Rokkitt",Georgia,serif;font-size:14.5px;line-height:18px;text-align:justify;color:#666}

.login-band{left:0;top:388px;width:900px;height:194px;background:var(--lime)}
.panel{position:absolute;background:var(--box);border-radius:10px;border:3px solid #fff;box-shadow:0 0 0 1px var(--box-line) inset}
.panel-title{position:absolute;width:100%;text-align:center;font-family:"Rokkitt",Georgia,serif;font-size:19px;color:var(--green)}
.field{position:absolute;left:15px;width:194px;height:18px;background:#fff;border:1px solid #ddd;font-size:10px;color:#666;padding:2px 7px}
.or{left:322px;top:462px;font-family:"Rokkitt",Georgia,serif;font-size:32px;color:#fff}
.provider{position:absolute;top:48px;width:80px;text-align:center}
.provider .mark{height:30px;display:flex;align-items:center;justify-content:center;font-family:"Rokkitt",Georgia,serif;font-weight:700;font-size:15px;color:var(--grey-dark)}
.provider .label{margin-top:12px;font-family:"Rokkitt",Georgia,serif;font-size:14px;color:#666}
.more{position:absolute;left:176px;top:120px;background:#e8e0c0;border-radius:8px;font-size:10px;color:#666;padding:1px 8px}

.section-head{font-family:"Rokkitt",Georgia,serif;font-size:19px;color:var(--green)}
.post{position:absolute;top:639px;width:188px}
.post-img{height:88px;border-radius:9px;border:3px solid #eee8d8}
.post h3{margin-top:16px;font-weight:normal;font-size:11.5px;line-height:14px;color:var(--cyan)}
.post p{margin-top:16px;font-size:9.6px;line-height:12.6px;text-align:justify;color:#555}
.post p b{color:var(--cyan)}
.share-item{position:absolute;left:722px;width:78px;display:flex;align-items:center;justify-content:center;color:#fff;font-family:"Rokkitt",Georgia,serif;font-size:16px}

.footer{left:0;top:878px;width:900px;height:322px;background:var(--grey);border-top:6px dotted #bbb}
.foot-head{position:absolute;top:898px;font-family:"Rokkitt",Georgia,serif;font-size:19px;color:#fff}
.foot-links{left:91px;top:934px;list-style:none;font-size:11.5px;line-height:18px;color:#fff}
.foot-links a{color:#8fe0f8;text-decoration:none}
.social{position:absolute;width:38px;height:38px;border-radius:50%;display:flex;align-items:center;justify-content:center;font-size:8px;color:#fff;box-shadow:0 2px 3px rgba(0,0,0,.3)}
.input{position:absolute;left:420px;width:187px;background:#6a6a6a;border:1px solid #777;border-radius:13px;font-size:11px;color:#ccc;padding:7px 15px}
.legal{left:92px;top:1122px;font-size:11px;color:#e0e0e0}
</style>
</head>
<body>

<header class="header abs"></header>
<div class="brand abs">zMatchy</div>
<div class="brand-sub abs">zMatchy.net</div>
<nav class="nav">
  <a style="left:392px">Why</a>
  <a style="left:465px">How It Works</a>
  <a style="left:615px">Our Blog</a>
</nav>
<a class="btn btn-green" style="left:720px;top:62px;width:90px;height:33px;font-size:19px">Sign Up</a>

<section class="hero abs"></section>
<svg class="abs" style="left:54px;top:236px" width="36" height="56" viewBox="0 0 36 56"><path d="M30 4 L6 28 L30 52" fill="none" stroke="#fff" stroke-width="7" stroke-linejoin="round" stroke-linecap="round"/><path d="M30 4 L6 28 L30 52" fill="none" stroke="#e6e2d8" stroke-width="2"/></svg>
<svg class="abs" style="left:810px;top:236px" width="36" height="56" viewBox="0 0 36 56"><path d="M6 4 L30 28 L6 52" fill="none" stroke="#fff" stroke-width="7" stroke-linejoin="round" stroke-linecap="round"/><path d="M6 4 L30 28 L6 52" fill="none" stroke="#e6e2d8" stroke-width="2"/></svg>
<div class="hero-frame abs"><div class="hero-photo" role="img" aria-label="Video still: a woman with open arms on a sunlit beach"></div></div>
<svg class="abs" style="left:244px;top:224px" width="64" height="80" viewBox="0 0 64 80"><path d="M4 4 L60 40 L4 76 Z" fill="rgba(255,255,255,.55)"/></svg>
<h1 class="hero-title abs slab" style="font-weight:normal">Find the love of your life</h1>
<p class="hero-sub abs">Lorem ipsum dolor sit amet, consectetur adipiscing elit.</p>
<p class="hero-copy abs">Praesent sollicitudin purus et orci consectetur at vulputate felis bibendum. Nullam posuere, nunc at egestas ultricies, tellus justo mollis ligula, quis congue nulla tellus a mauris. Ut facilisis odio a orci euismod vehicula.</p>
<a class="btn btn-cyan" style="left:683px;top:333px;width:113px;height:35px;font-size:19px">Get Started</a>

<section class="login-band abs"></section>
<div class="panel" style="left:90px;top:409px;width:225px;height:151px">
  <div class="panel-title" style="top:16px">Member Login</div>
  <div class="field" style="top:50px">Username...</div>
  <div class="field" style="top:77px">Password...</div>
  <a class="btn btn-cyan" style="left:71px;top:103px;width:82px;height:26px;font-size:14px">Log In</a>
</div>
<div class="or abs">or</div>
<div class="panel" style="left:367px;top:409px;width:443px;height:151px">
  <div class="panel-title" style="top:16px">Log In using...</div>
  <div class="provider" style="left:13px"><div class="mark">Facelink</div><div class="label">Facelink</div></div>
  <div class="provider" style="left:98px"><div class="mark">Postbox</div><div class="label">Postbox</div></div>
  <div class="provider" style="left:185px"><div class="mark">Yodelo</div><div class="label">Yodelo</div></div>
  <div class="provider" style="left:269px"><div class="mark">KeyPass</div><div class="label">KeyPass</div></div>
  <div class="provider" style="left:348px"><div class="mark">Roomly</div><div class="label">Roomly</div></div>
  <div class="more">more ▾</div>
</div>

<h2 class="section-head abs" style="left:90px;top:598px;font-weight:normal">Recent blog posts</h2>
<h2 class="section-head abs" style="left:734px;top:598px;font-weight:normal">Share</h2>

<article class="post" style="left:90px">
  <div class="post-img" role="img" aria-label="Photo: a country path through green fields at sunset" style="background:linear-gradient(#f4d870,#d8c060 45%,#7fa83a 60%,#5d8c2a)"></div>
  <h3>The light at the end of the tunnel</h3>
  <p>Lorem ipsum dolor sit amet, consectetur adipiscing elit. Phasellus orci urna, sollicitudin ut sodales eu, porttitor id lorem. Donec nulla urna, rutrum vitae pharetra sit amet, feugiat eget nulla. <b>»</b></p>
</article>
<article class="post" style="left:292px">
  <div class="post-img" role="img" aria-label="Photo: a woman raising her arms on a tropical beach" style="background:linear-gradient(#3e8fd8,#8cc8ee 50%,#56c0d0 65%,#f2e6c8 75%)"></div>
  <h3>Be happy alone. Then find someone else to be happy with.</h3>
  <p>Lorem ipsum dolor sit amet, consectetur adipiscing elit. Phasellus orci urna, sollicitudin ut sodales eu, porttitor id lorem. Donec nulla urna, rutrum vitae pharetra sit amet, feugiat eget nulla. <b>»</b></p>
</article>
<article class="post" style="left:495px">
  <div class="post-img" role="img" aria-label="Photo: a man cooking in a bright kitchen" style="background:linear-gradient(90deg,#e8e8e4,#c8c4bc 50%,#f2f2ee)"></div>
  <h3>How to be a real man</h3>
  <p>Lorem ipsum dolor sit amet, consectetur adipiscing elit. Phasellus orci urna, sollicitudin ut sodales eu, porttitor id lorem. Donec nulla urna, rutrum vitae pharetra sit amet, feugiat eget nulla. <b>»</b></p>
</article>

<div class="share-item" style="top:640px;height:56px;background:var(--cyan);border-radius:14px">Like</div>
<div class="share-item" style="top:720px;height:56px;background:#e8a830;border-radius:6px">Chirpa</div>
<div class="share-item" style="top:802px;left:730px;width:60px;height:38px;background:#3a8fd0;border-radius:5px">Plusio</div>

<footer class="footer abs"></footer>
<div class="foot-head" style="left:91px">Read More</div>
<div class="foot-head" style="left:241px">Share the Love</div>
<div class="foot-head" style="left:473px">Let's Talk</div>
<ul class="foot-links abs">
  <li>» <a>Why zMatchy</a></li>
  <li>» <a>How it works</a></li>
  <li>» <a>Sign Up</a></li>
  <li>» <a>Login</a></li>
  <li>» <a>About Us</a></li>
</ul>
<div class="social" style="left:235px;top:929px;background:#2a4a8c">Facelink</div>
<div class="social" style="left:287px;top:929px;background:#7fd2e8">Chirpa</div>
<div class="social" style="left:338px;top:929px;background:#1e3a8a">Roomly</div>
<div class="social" style="left:235px;top:982px;background:#2f8a3a">Tumbla</div>
<div class="social" style="left:287px;top:982px;background:#1e6fa8">Linkora</div>
<div class="social" style="left:338px;top:982px;background:#1e3a6a">Markly</div>
<div class="social" style="left:235px;top:1034px;background:#d8d8d8;color:#555">Panea</div>
<div class="social" style="left:287px;top:1034px;background:#333">Tastr</div>
<div class="social" style="left:338px;top:1034px;background:#f07a14">Feed</div>

<div class="input" style="top:929px;height:26px;padding-top:6px">Your name...</div>
<div class="input" style="top:963px;height:26px;padding-top:6px">Your email...</div>
<div class="input" style="top:996px;height:105px">Your message...</div>
<a class="btn btn-pink" style="left:473px;top:1117px;width:82px;height:27px;font-size:14px">Send</a>

<div class="abs" style="left:638px;top:895px;font-family:'Rokkitt',Georgia,serif;font-size:44px;font-weight:700;color:#fff">zMatchy</div>
<div class="abs" style="left:659px;top:960px;font-size:11px;color:#e6e6e6">All right reserved © 2011</div>
<div class="legal abs">Terms of Service &nbsp; | &nbsp; Privacy Policy</div>

</body>
</html>
```